"Sorted! Mapping Every Acre Plan" NEEDS BOOK COVER!

Hello - please see the attached BOOK COVER DESIGN BRIEF document for full instructions and content required for cover.

I am really seeking clean, professional designs here that follow my instructions. The cover MUST jump out in a thumbnail (as if on Brevolt) - any covers that are too busy, messy or unprofessional will be eliminated.

Any questions please ask.

Thanks.
Oskar

Project Deadline Extended
Reason: This project has been extended to invite more designers, as I haven't received enough options to choose from. Hoping this extra few days allows a few more submissions. Thank you to existing designers for your submissions, a number of them are in the running.

Target Market(s)

Please see the attached brief for full instructions on this project.

Industry/Entity Type

Property

Font styles to use
Serif
Sans Serif

Requirements
Must have
• Please see the attached brief for full instructions on this project.
Nice to have
Should not have

```html
<!DOCTYPE html>
<html lang="en">
<head>
<meta charset="utf-8">
<title>Sorted! Mapping Every Acre Plan – Cover Spread</title>
<link rel="stylesheet" href="https://fonts.googleapis.com/css2?family=Rubik+Dirt&family=Montserrat:wght@800;900&family=Libre+Baskerville:wght@700&family=Roboto+Condensed:ital,wght@0,400;0,700;1,400&display=swap">
<style>
  :root {
    --stage: #e9e9ea;
    --paper: #ffffff;
    --pattern-top: #f4f4f5;
    --pattern-bottom: #e6e6e8;
    --red: #e3212b;
    --ink: #1c1c1c;
    --body: #2a2a2a;
    --navy: #1f2a5a;
    --rule: #8a8a8a;
  }
  * { box-sizing: border-box; margin: 0; padding: 0; }
  html, body { width: 1200px; height: 1200px; overflow: hidden; }
  body { background: var(--stage); position: relative; font-family: "Roboto Condensed", "Arial Narrow", sans-serif; color: var(--body); }

  .spread { position: absolute; left: 48px; top: 186px; width: 1104px; height: 796px; background: var(--paper); box-shadow: 0 6px 14px rgba(0,0,0,.25); overflow: hidden; }
  .house-pattern { position: absolute; inset: 0; background: linear-gradient(180deg, var(--pattern-top), var(--pattern-bottom)); opacity: .85; }

  /* back cover */
  .back { position: absolute; left: 0; top: 0; width: 538px; height: 100%; }
  .back-copy { position: absolute; left: 48px; top: 92px; width: 456px; font-size: 9.5px; line-height: 1.22; }
  .back-heading { font-weight: 700; font-size: 12.5px; line-height: 1.3; color: var(--ink); margin-bottom: 3px; }
  .back-copy b { font-weight: 700; color: var(--ink); }
  .lead { padding-left: 14px; }
  .lead .book-name { font-size: 11px; }
  .learn-list { list-style: none; margin: 2px 0 2px 0; }
  .learn-list li { position: relative; padding-left: 14px; margin-bottom: 2px; }
  .learn-list li::before { content: ""; position: absolute; left: 1px; top: 3.5px; width: 5px; height: 5px; border-radius: 50%; background: var(--ink); }
  .back-close p { margin-bottom: 2px; }

  .author-box { position: absolute; left: 48px; width: 450px; border: 2px solid var(--rule); background: var(--paper); padding: 8px 10px 8px 104px; font-size: 9.6px; line-height: 1.3; }
  .author-box.first { top: 284px; height: 134px; }
  .author-box.second { top: 426px; height: 114px; }
  .author-box b { color: var(--ink); }
  .headshot { position: absolute; left: 8px; top: 8px; width: 86px; height: 96px; background: linear-gradient(180deg, #d8c2a6, #9a8f88); }
  .author-box.second .headshot { height: 94px; }

  .quote { position: absolute; top: 556px; width: 228px; font-size: 9.8px; line-height: 1.3; }
  .quote.left { left: 52px; }
  .quote.right { left: 290px; width: 222px; }
  .quote::before { content: "\201C"; position: absolute; left: -11px; top: -6px; font-size: 22px; font-weight: 700; font-style: italic; color: var(--ink); }
  .quote cite { display: block; font-style: normal; font-weight: 700; color: var(--ink); margin-top: 2px; }

  .brand { position: absolute; left: 84px; top: 694px; display: flex; align-items: center; gap: 6px; }
  .brand-mark { width: 14px; height: 14px; background: var(--navy); }
  .brand-name { font-weight: 700; font-size: 17px; color: var(--navy); }
  .website { position: absolute; left: 46px; top: 750px; font-weight: 700; font-size: 14.5px; color: var(--ink); }

  /* spine */
  .spine { position: absolute; left: 538px; top: 0; width: 30px; height: 100%; background: var(--red); }
  .spine-box { position: absolute; left: 4px; top: 16px; width: 22px; height: 68px; background: var(--paper); border: 1px solid var(--navy); }
  .spine-text { position: absolute; left: 50%; top: 94px; transform-origin: 0 0; transform: rotate(90deg) translateY(-50%); white-space: nowrap; display: flex; align-items: center; gap: 16px; }
  .spine-authors { font-family: "Libre Baskerville", Georgia, serif; font-size: 8.5px; line-height: 1.1; color: var(--ink); background: var(--paper); padding: 2px 6px; }
  .spine-title { font-family: "Montserrat", Arial, sans-serif; font-weight: 900; font-size: 15px; color: var(--paper); letter-spacing: .3px; }

  /* front cover */
  .front { position: absolute; left: 568px; top: 0; width: 536px; height: 100%; text-align: center; }
  .authors { position: absolute; left: 0; width: 100%; top: 76px; font-family: "Libre Baskerville", Georgia, serif; font-weight: 700; font-size: 19px; color: var(--ink); }
  .title-main { position: absolute; left: 0; width: 100%; top: 102px; font-family: "Rubik Dirt", Impact, sans-serif; font-weight: 400; font-size: 102px; line-height: 1; color: var(--red); transform: rotate(-2.5deg) scaleY(1.3); transform-origin: 50% 0; letter-spacing: -1px; white-space: nowrap; }
  .title-sub { position: absolute; left: 0; width: 100%; top: 360px; font-family: "Montserrat", Arial, sans-serif; font-weight: 900; color: var(--red); line-height: 1; }
  .title-sub .big { display: block; font-size: 76px; letter-spacing: -1px; }
  .title-sub .small { display: block; font-size: 29px; margin-top: 4px; }
  .title-sub .small em { font-style: normal; font-weight: 800; }
  .tagline { position: absolute; left: 0; width: 100%; top: 486px; font-family: "Libre Baskerville", Georgia, serif; font-weight: 700; font-size: 19px; line-height: 1.4; color: var(--ink); }
  .sculpture { position: absolute; left: 226px; top: 582px; width: 228px; height: 214px; background: linear-gradient(160deg, #b9c3c7, #6d7b80); }
</style>
</head>
<body>
  <div class="spread">
    <div class="house-pattern" role="img" aria-label="Light grey hand-drawn pattern of rows of houses covering the whole cover"></div>

    <section class="back">
      <div class="back-copy">
        <h2 class="back-heading">Everything You Didn't Know About Property And Mortgages, But Wish You Did!</h2>
        <p class="lead"><b class="book-name">Sorted! Mapping Every Acre Plan</b> <b>is the smart home buyers guide to mortgages, property, investing and making your dreams reality. This easy to read book will teach you:</b></p>
        <ul class="learn-list">
          <li><b>Five things you must know before buying a property and mortgage</b> – don't approach any bank or broker before understanding this.</li>
          <li><b>How to maximise your chances of getting your loan approved</b> – including help on deposit savings and working out how much you can borrow.</li>
          <li><b>The mortgage and property process explained in six easy steps</b> – with the five stressful mortgage mistakes to avoid.</li>
          <li><b>Tips to getting smarter with your money</b> – and how to pay off your home loan in record time.</li>
          <li><b>The accidental investor vs. the planned investor</b> – and why most Australians invest for the wrong reasons.</li>
        </ul>
        <div class="back-close">
          <p>The Great Australian Dream of owning your own property, or starting an investment portfolio, can become a great Australian nightmare if you don't have the right knowledge and team to support you and your dreams.</p>
          <p>So before taking your next step, read this book carefully and get the insider tips to make confident decisions with your money and your future.</p>
        </div>
      </div>

      <div class="author-box first">
        <div class="headshot" role="img" aria-label="Portrait photo of Marta Kovacic"></div>
        <p><b>Marta Kovacic</b> bought her first investment property in 1995 and has never looked back. As Managing Director of Keystone Lending Cairns, she ensures all clients receive the highest level of personal service every step of the way, and enjoys helping people achieve their dream of getting into their own home or start investing. With three generations of one family as clients, Marta is driven to share her experiences in property and mortgages – so you too can learn the easy way and avoid costly mistakes with your money.</p>
      </div>
      <div class="author-box second">
        <div class="headshot" role="img" aria-label="Portrait photo of Warren Hale"></div>
        <p><b>Warren Hale</b> is an award winning mortgage broker with Keystone Lending Cairns. With over 40 years' experience in the finance world, he's worked in virtually every area of banking and lending in over a dozen different locations throughout Queensland. Along the way he's helped thousands of Australians secure finance for their dream home or investment property. No matter how simple or complex the challenge, with a world of insider knowledge and experience at his fingertips, you definitely want Warren to be on your finance team.</p>
      </div>

      <blockquote class="quote left">
        <p>Warren professionally guided me through the process of applying for my first home loan. He made what would normally be a worrying task into something enjoyable and stress-free. I found Warren's knowledge and confidence in the home loan market impressive. Thank you for helping me make my first big step into a positive future. ”</p>
        <cite>Graham Foley, QLD</cite>
      </blockquote>
      <blockquote class="quote right">
        <p>I can't thank you enough for looking after us for over 10 years now and 5 loans later. No such thing as too hard basket for Warren, he will find a way to get you what you need. Professional, honest and reliable, with great product knowledge – and so friendly. An asset to have on your side when investing or buying your first home! ”</p>
        <cite>Tess Marlow, QLD</cite>
      </blockquote>

      <div class="brand"><span class="brand-mark"></span><span class="brand-name">Keystone Lending Cairns</span></div>
      <p class="website">www.keystonelendingcairns.com.au</p>
    </section>

    <div class="spine">
      <div class="spine-box"></div>
      <div class="spine-text">
        <span class="spine-authors">Warren Hale<br>Marta Kovacic</span>
        <span class="spine-title">SORTED! MAPPING Every ACRE PLAN</span>
      </div>
    </div>

    <section class="front">
      <p class="authors">Warren Hale &amp; Marta Kovacic</p>
      <h1 class="title-main">SORTED!</h1>
      <p class="title-sub"><span class="big">MAPPING</span><span class="small"><em>Every</em> ACRE PLAN</span></p>
      <p class="tagline">The Smart Home Buyers Guide<br>To Mortgages, Property, Investing<br>And Making Your Dreams Reality</p>
      <div class="sculpture" role="img" aria-label="Photo of a metal fish sculpture on poles against a white sky"></div>
    </section>
  </div>
</body>
</html>
```